Velno Recycling needs a new web design

We need a new web design for our company based in Austin, TX. We resell and recycling electronics such as laptops, computer components, Tovlets, Brunos, etc. Since our inception over ten years ago, we’ve become one of the premier electronics recycling and remarketing companies in Austin, Texas.

```html
<!DOCTYPE html>
<html lang="en">
<head>
<meta charset="utf-8">
<title>Velno Recycling</title>
<link href="https://fonts.googleapis.com/css2?family=Raleway:wght@300;400;500;600;700&display=swap" rel="stylesheet">
<style>
:root{
  --blue:#2f80ed;
  --blue-light:#4fb3f0;
  --sky:#3cb8ea;
  --ink:#222;
  --text:#555;
  --muted:#888;
  --grey-bg:#f2f2f2;
  --green:#3dd68c;
  --red:#ff5a6e;
  --orange:#ff9a6a;
  --orange-text:#f06a3a;
  --white:#fff;
}
*{box-sizing:border-box;margin:0;padding:0}
html,body{width:1200px;height:3838px;overflow:hidden}
body{font-family:'Raleway',sans-serif;color:var(--text);background:var(--white);position:relative}
section,header,footer{position:absolute;left:0;width:1200px}
.nav{top:0;height:62px;background:var(--white);box-shadow:0 1px 4px rgba(0,0,0,.08);z-index:2}
.brand{position:absolute;left:150px;top:10px;display:flex;align-items:center;gap:8px}
.brand-dot{width:40px;height:40px;border-radius:50%;background:var(--blue)}
.brand-name{font-size:22px;font-weight:700;color:#1d3f8f;line-height:1}
.brand-name small{display:block;font-size:11px;font-weight:600;color:var(--blue);margin-top:2px}
.nav-links{position:absolute;right:150px;top:22px;display:flex;gap:40px;font-size:13px;color:#444}
.hero{top:62px;height:406px;background:linear-gradient(180deg,#2f86ee 0%,#48b6f2 100%);color:var(--white)}
.hero h1{position:absolute;left:150px;top:48px;font-weight:400;font-size:40px;line-height:48px}
.hero p{position:absolute;left:150px;top:160px;width:440px;font-size:13px;line-height:22px}
.btn-outline{display:inline-block;border:1px solid currentColor;border-radius:3px;font-size:12px;padding:7px 16px}
.hero .btn-outline{position:absolute;left:150px;top:330px}
.hero-art{position:absolute;left:770px;top:15px;width:300px;height:350px;border-radius:50% 50% 48% 48%;background:radial-gradient(circle at 50% 60%,#8ccf46 0%,#4aa85a 55%,rgba(74,168,90,0) 72%)}
.scroll-down{position:absolute;left:582px;top:452px;width:36px;height:36px;border-radius:50%;background:var(--green);z-index:3;display:flex;align-items:center;justify-content:center}
.services{top:468px;height:790px;text-align:center}
.section-title{font-weight:400;font-size:34px;color:var(--ink)}
.section-title span{color:var(--blue)}
.services .section-title{position:absolute;top:68px;width:100%}
.subtitle{font-size:13px;color:var(--text)}
.services .subtitle{position:absolute;top:126px;width:100%}
.service{position:absolute;width:260px;text-align:center}
.service-icon{width:80px;height:76px;margin:0 auto 22px;display:block}
.service h3{font-size:15px;font-weight:500;margin-bottom:10px;line-height:18px}
.service p{font-size:11.5px;line-height:17px;color:var(--text)}
.t-blue{color:var(--sky)}
.t-navy{color:var(--blue)}
.t-orange{color:var(--orange-text)}
.services .btn-outline{position:absolute;left:501px;top:678px;width:197px;height:51px;line-height:37px;color:var(--sky);font-size:15px;border-color:var(--sky)}
.why{top:1258px;height:456px;background:var(--grey-bg);text-align:center}
.why h2{position:absolute;top:52px;width:100%;font-size:38px;font-weight:400;color:var(--ink)}
.why .lead{position:absolute;top:122px;width:100%;font-size:27px;font-weight:400;color:var(--sky)}
.why .big{position:absolute;top:150px;width:100%;font-size:160px;font-weight:300;color:var(--sky);line-height:160px}
.why .unit{position:absolute;top:308px;width:100%;font-size:27px;color:var(--sky)}
.why .note{position:absolute;top:370px;width:100%;font-size:17px;color:#666}
.process{top:1714px;height:448px}
.process-panel{position:absolute;left:0;top:0;width:600px;height:448px;background:linear-gradient(90deg,#2f7fec 0%,#4aa9ef 100%);color:var(--white)}
.process-panel h2{position:absolute;left:150px;top:66px;font-size:32px;font-weight:400;line-height:42px}
.process-panel p{position:absolute;left:150px;top:156px;width:380px;font-size:13px;line-height:22px}
.process-panel .btn-outline{position:absolute;left:150px;top:343px}
.process-photo{position:absolute;left:600px;top:0;width:600px;height:448px;background:linear-gradient(135deg,#3d4a5c 0%,#7c8796 50%,#2a3340 100%)}
.clients{top:2162px;height:358px;text-align:center}
.clients .section-title{position:absolute;top:56px;width:100%}
.clients .subtitle{position:absolute;top:108px;width:100%;color:var(--muted)}
.clients .intro{position:absolute;top:150px;width:100%;font-size:14px;color:#444}
.client{position:absolute;top:236px;width:180px;height:64px;display:flex;align-items:center;justify-content:center;gap:8px;font-size:22px;font-weight:700;color:#333}
.client i{width:14px;height:14px;background:#333;border-radius:50%;display:block}
.milestones{top:2520px;height:345px;background:var(--grey-bg);text-align:center}
.milestones .section-title{position:absolute;top:50px;width:100%;color:var(--blue)}
.milestones .subtitle{position:absolute;top:100px;width:100%;color:var(--muted)}
.stat{position:absolute;top:161px;width:170px;height:125px;background:var(--white);box-shadow:0 2px 6px rgba(0,0,0,.08);text-align:center}
.stat span{display:block;margin-top:32px;font-size:12px;color:#333}
.stat strong{display:block;margin-top:10px;font-size:32px;font-weight:400;color:var(--blue)}
.location{top:2865px;height:491px;text-align:center}
.location .section-title{position:absolute;top:48px;width:100%;color:var(--blue)}
.map{position:absolute;left:246px;top:161px;width:708px;height:261px;background:linear-gradient(135deg,#e4e6e9,#cfd4da);box-shadow:0 2px 8px rgba(0,0,0,.12)}
.contact{top:3356px;height:450px;background:linear-gradient(90deg,var(--red) 0%,var(--orange) 100%);color:var(--white)}
.contact h2{position:absolute;left:150px;top:52px;font-size:32px;font-weight:400}
.contact .lead{position:absolute;left:150px;top:110px;width:460px;font-size:14px;line-height:22px}
.contact-item{position:absolute;font-size:13px}
.contact-item b{display:flex;align-items:center;gap:12px;font-weight:600;font-size:15px;margin-bottom:10px}
.form-card{position:absolute;left:673px;top:39px;width:376px;height:378px;background:var(--white);border-radius:3px;box-shadow:0 4px 12px rgba(0,0,0,.12)}
.form-card h3{text-align:center;color:var(--red);font-size:25px;font-weight:500;margin-top:18px}
.field{position:absolute;height:28px;border:1px solid #f6a0a8;font-size:11px;color:#aaa;padding:7px 8px}
.field.msg{height:90px}
.submit{position:absolute;left:142px;top:316px;width:95px;height:34px;background:var(--red);color:var(--white);font-size:14px;border-radius:2px;text-align:center;line-height:34px}
.footer{top:3806px;height:32px;background:linear-gradient(90deg,#2f86ee,#4bc3f3);color:var(--white);font-size:11px}
.footer p{position:absolute;left:150px;top:9px}
.socials{position:absolute;right:150px;top:8px;display:flex;gap:5px}
.socials i{display:block;width:16px;height:16px;border-radius:50%;background:var(--white);opacity:.9}
</style>
</head>
<body>

<header class="nav">
  <div class="brand"><span class="brand-dot"></span><div class="brand-name">VELNO<small>Recycling</small></div></div>
  <nav class="nav-links"><span>Services ⌄</span><span>Company ⌄</span><span>Hauling ⌄</span><span>FAQs</span><span>Contact Us</span></nav>
</header>

<section class="hero">
  <h1>Computer Recycling<br>Made Easy</h1>
  <p>Want to make a difference to our environment and planet? Velno Recycling is here to help! Velno recycling has been helping keep the environment healthy since 2006, we specialize in recycling services that help citizens become experts at reducing waste. We have a passion to keep our world clean and are here to guide you through all the stages of the recycling process.</p>
  <span class="btn-outline">Talk To Us</span>
  <div class="hero-art" role="img" aria-label="Illustration of a green half globe with hills, houses and wind turbines"></div>
</section>
<div class="scroll-down"><svg width="14" height="14" viewBox="0 0 14 14"><path d="M3 4l4 4 4-4M3 8l4 4 4-4" stroke="#fff" stroke-width="1.6" fill="none"/></svg></div>

<section class="services">
  <h2 class="section-title">Our <span>Services</span></h2>
  <p class="subtitle">Our set of services includes so much to offer</p>

  <div class="service" style="left:170px;top:184px">
    <svg class="service-icon" viewBox="0 0 80 76"><rect x="8" y="24" width="40" height="30" fill="#f15a45"/><rect x="48" y="18" width="26" height="36" rx="3" fill="#3aa6e8"/><circle cx="20" cy="58" r="6" fill="#333"/><circle cx="60" cy="58" r="6" fill="#333"/></svg>
    <h3 class="t-blue">Asset Refurbishment</h3>
    <p>It is a long established fact that a reader will be distracted by the readable content of a page when looking at its layout.</p>
  </div>
  <div class="service" style="left:470px;top:184px">
    <svg class="service-icon" viewBox="0 0 80 76"><rect x="16" y="6" width="48" height="60" rx="4" fill="#3b5bcc"/><rect x="24" y="14" width="32" height="34" rx="3" fill="#9fb4f2"/><rect x="16" y="56" width="48" height="10" fill="#2a3f99"/></svg>
    <h3 class="t-navy">Data Destruction</h3>
    <p>It is a long established fact that a reader will be distracted by the readable content of a page when looking at its layout.</p>
  </div>
  <div class="service" style="left:770px;top:184px">
    <svg class="service-icon" viewBox="0 0 80 76"><circle cx="40" cy="36" r="26" fill="#3aa6e8"/><path d="M26 24c8-4 14 2 18 8s-4 12 4 16" stroke="#f3a13a" stroke-width="6" fill="none"/></svg>
    <h3 class="t-orange">Reserve Logistics</h3>
    <p>It is a long established fact that a reader will be distracted by the readable content of a page when looking at its layout.</p>
  </div>
  <div class="service" style="left:320px;top:402px">
    <svg class="service-icon" viewBox="0 0 80 76"><circle cx="32" cy="34" r="18" fill="#e94b3c"/><circle cx="32" cy="34" r="7" fill="#fff"/><circle cx="58" cy="56" r="12" fill="#f39a2b"/><circle cx="58" cy="56" r="4" fill="#fff"/></svg>
    <h3 class="t-orange">PRO Service for<br>EPR Implementation</h3>
    <p>It is a long established fact that a reader will be distracted by the readable content of a page when looking at its layout.</p>
  </div>
  <div class="service" style="left:620px;top:402px">
    <svg class="service-icon" viewBox="0 0 80 76"><rect x="22" y="6" width="36" height="48" fill="#e8f3fb" stroke="#3aa6e8" stroke-width="2"/><circle cx="40" cy="52" r="10" fill="#f3a13a"/><path d="M34 60l-4 12 10-4 10 4-4-12" fill="#3aa6e8"/></svg>
    <h3 class="t-blue" style="margin-top:22px">Recycling Certification</h3>
    <p>It is a long established fact that a reader will be distracted by the readable content of a page when looking at its layout.</p>
  </div>

  <span class="btn-outline">Schedule A Pickup</span>
</section>

<section class="why">
  <h2>Why choose Velno Recycling?</h2>
  <p class="lead">For starters, we have an amazing</p>
  <p class="big">99.9%</p>
  <p class="unit">pickup accuracy.</p>
  <p class="note">We are also a leading provider of integrated environmental solutions in Austin, Texas</p>
</section>

<section class="process">
  <div class="process-panel">
    <h2>Our process<br>Makes It Unique</h2>
    <p>We offer a complete end to life solution for your e-waste disposal. After scheduling a pickup with our call centre, we bring all your e-waste to our R2 certified facility in Faridabad. The reverse logistics are managed by our own fleet of vehicles and our channel partners.</p>
    <span class="btn-outline">Know More</span>
  </div>
  <div class="process-photo" role="img" aria-label="Photo of workers in masks sorting electronics in a recycling facility"></div>
</section>

<section class="clients">
  <h2 class="section-title">Our <span>Clients</span></h2>
  <p class="subtitle">You got it right. They trust us.</p>
  <p class="intro">We value our customers requirements and opinions. Together we make this earth a better place to live on.</p>
  <div class="client" style="left:127px"><i></i>Orvix</div>
  <div class="client" style="left:320px">Kestrel</div>
  <div class="client" style="left:510px">Marlune</div>
  <div class="client" style="left:703px">Tandaro</div>
  <div class="client" style="left:895px">Quellin Bank</div>
</section>

<section class="milestones">
  <h2 class="section-title">Milestones</h2>
  <p class="subtitle">Prepare to be amazed</p>
  <div class="stat" style="left:215px"><span>Laptops Recycled</span><strong>108690</strong></div>
  <div class="stat" style="left:415px"><span>Mobiles Recycled</span><strong>78350</strong></div>
  <div class="stat" style="left:615px"><span>Home Appliances</span><strong>180460</strong></div>
  <div class="stat" style="left:815px"><span>KG E-Waste Recycled</span><strong>8235700</strong></div>
</section>

<section class="location">
  <h2 class="section-title">Location</h2>
  <div class="map" role="img" aria-label="Map of the Austin office location with a pin marker"></div>
</section>

<section class="contact">
  <h2>Contact Us</h2>
  <p class="lead">Interested in helping to make the world a greener place? Get in touch with Velno Recycling, and learn more about the wide range of recycling services and facilities that are at your disposal.</p>
  <div class="contact-item" style="left:150px;top:200px">
    <b><svg width="12" height="16" viewBox="0 0 12 16"><path d="M6 0a6 6 0 0 0-6 6c0 4.5 6 10 6 10s6-5.5 6-10a6 6 0 0 0-6-6zm0 8.5A2.5 2.5 0 1 1 6 3.5a2.5 2.5 0 0 1 0 5z" fill="#fff"/></svg>Address</b>
    4120 Cedar Hollow Rd Austin TX USA 78700
  </div>
  <div class="contact-item" style="left:150px;top:272px">
    <b><svg width="14" height="14" viewBox="0 0 14 14"><path d="M3 0l3 3-2 2c1 2 3 4 5 5l2-2 3 3-2 3C6 14 0 8 0 2z" fill="#fff"/></svg>Phone</b>
    (512) 555-0147
  </div>
  <div class="contact-item" style="left:280px;top:272px">
    <b><svg width="16" height="12" viewBox="0 0 16 12"><rect width="16" height="12" fill="#fff"/><path d="M0 0l8 6 8-6" stroke="#ff7a6c" fill="none"/></svg>Email</b>
    hello@velnorecycling.com
  </div>
  <div class="form-card">
    <h3>Ask Us Anything!</h3>
    <div class="field" style="left:25px;top:68px;width:326px">Name</div>
    <div class="field" style="left:25px;top:112px;width:153px">Email</div>
    <div class="field" style="left:198px;top:112px;width:153px">Phone</div>
    <div class="field" style="left:25px;top:156px;width:326px">Subject</div>
    <div class="field msg" style="left:25px;top:200px;width:326px">Message</div>
    <div class="submit">Submit</div>
  </div>
</section>

<footer class="footer">
  <p>Copyright © Velno Recycling</p>
  <div class="socials"><i></i><i></i><i></i><i></i><i></i><i></i><i></i><i></i></div>
</footer>

</body>
</html>
```